BLRK 2014 Holiday Card

About the Organization: Stone Tales That Shine, LLC helps nature protection and pollution control organizations professionalize and modernize their communications. They assist organizations on fundraising, issue advocacy, or pollution prevention campaigns!

Project Summary: Stone Tales That Shine would like to take stock and thank the amazing group of clients we have worked with and prospects who we are close to closing deals with. BLRK would like to show their appreciation in a holiday card.

Project Timing: BLRK would like to mail the holiday cards by November 14, 2014.

Target Audience: The target audience is the clients that we have worked for this year. They work for environmental organizations. Most are government and non-governmental organizations.
Updates

Please provide inside and outside mock ups. We look forward to reviewing your designs.

Target Market(s)

The target audience is the clients that we have worked for this year. They work for environmental organizations. Most are government and non-governmental organizations.

Industry/Entity Type

Government

Requirements
Must have
• This holiday card must have 4 pages and use the photos as a guide.

Please follow the color and design elements provided in the BLRK_ArtHerdly_StrategyBriefHolidayCard_10102014.pdf.

I also provide the last two holiday cards and some sample image to guide the design.

You have two design choices for our logo. Both are also provided.

```html
<!DOCTYPE html>
<html lang="en">
<head>
<meta charset="utf-8">
<title>BLRK Holiday Card – Inside Spread</title>
<link rel="stylesheet" href="https://fonts.googleapis.com/css2?family=Cormorant+SC:wght@400;500&family=Dancing+Script:wght@500&display=swap">
<style>
  :root {
    --paper: #ffffff;
    --ink: #3a3a3a;
    --holiday-blue: #2a8fd6;
    --signature-tone: #e6e6e6;
  }
  html, body {
    margin: 0;
    padding: 0;
    overflow: hidden;
    background: var(--paper);
  }
  .card-spread {
    position: relative;
    width: 1200px;
    height: 900px;
    background: var(--paper);
    overflow: hidden;
  }
  .signature-panel {
    position: absolute;
    left: 0;
    top: 0;
    width: 600px;
    height: 900px;
  }
  .greeting-panel {
    position: absolute;
    left: 600px;
    top: 0;
    width: 600px;
    height: 900px;
    font-family: "Cormorant SC", "Times New Roman", serif;
    font-weight: 500;
    color: var(--ink);
    text-align: center;
  }
  .greeting-line {
    position: absolute;
    left: 0;
    width: 596px;
    margin: 0;
    font-size: 20px;
    letter-spacing: 0.5px;
    line-height: 1;
  }
  .thanks-1 { top: 323px; }
  .thanks-2 { top: 351px; }
  .thanks-3 { top: 379px; }
  .wish { top: 479px; }
  .holiday-title {
    position: absolute;
    left: 0;
    width: 596px;
    top: 502px;
    margin: 0;
    font-family: "Dancing Script", cursive;
    font-weight: 500;
    font-size: 36px;
    color: var(--holiday-blue);
    line-height: 1.1;
  }
  .team-sign-off { top: 553px; }
</style>
</head>
<body>
<main class="card-spread">
  <svg class="signature-panel" width="600" height="900" viewBox="0 0 600 900">
    <g fill="var(--signature-tone)">
      <rect role="img" aria-label="Handwritten signature of Owen Marsh" x="82" y="215" width="160" height="44" rx="22" transform="rotate(-22 162 237)"/>
      <rect role="img" aria-label="Handwritten signature of Dario Quent" x="305" y="220" width="245" height="46" rx="23" transform="rotate(12 427 243)"/>
      <rect role="img" aria-label="Handwritten signature of Lena Thorvik" x="178" y="318" width="310" height="50" rx="25"/>
      <rect role="img" aria-label="Handwritten signature of Paul Venner" x="48" y="468" width="166" height="36" rx="18" transform="rotate(-14 131 486)"/>
      <rect role="img" aria-label="Handwritten signature of Nora Pell" x="324" y="430" width="210" height="52" rx="26" transform="rotate(-10 429 456)"/>
      <rect role="img" aria-label="Handwritten signature of Tessa Lume" x="154" y="552" width="188" height="36" rx="18"/>
      <rect role="img" aria-label="Handwritten signature of Ilsa Roan" x="334" y="626" width="200" height="46" rx="23" transform="rotate(8 434 649)"/>
      <rect role="img" aria-label="Handwritten signature of Mira Caldwell" x="132" y="690" width="195" height="34" rx="17"/>
    </g>
  </svg>

  <section class="greeting-panel" aria-label="Holiday greeting">
    <p class="greeting-line thanks-1">As this year draws to a close,</p>
    <p class="greeting-line thanks-2">we are grateful for the opportunities</p>
    <p class="greeting-line thanks-3">we have had to work together.</p>
    <p class="greeting-line wish">We wish you all the best for the year to come.</p>
    <h1 class="holiday-title">Happy Holidays</h1>
    <p class="greeting-line team-sign-off">from the Stone Tales That Shine team</p>
  </section>
</main>
</body>
</html>
```